Financial services firm needs updated web design

Our current website, coinpathwealth.example was created by ourselves using templates provided by our website host, Harborline Webworks. We are looking to get a whole new look and feel to our website that is clean, professional and easy to navigate. The design must be able to be transferred to Harborline Webworks for hosting (FTP??-outside my area of expertise - sorry) and that the information can be updated and changed by ourselves in the future. I have included our updated logo and our business card design.
Updates
Project Deadline Extended
Reason: Went away on vacation for two weeks.
Target Market(s)
Age 50+ individuals looking for investment, retirement and estate planning guidance.
Industry/Entity Type
Financial
Number of Pages Required
1 page
Font styles to use
Other font styles liked:
- Adobe Caslon Pro
Look and feel
Each slider illustrates characteristics of the customer's brand and the style your logo design should communicate.

```html
<!DOCTYPE html>
<html lang="en">
<head>
<meta charset="utf-8">
<title>Alderbrook Advisors</title>
<link rel="stylesheet" href="https://fonts.googleapis.com/css2?family=Open+Sans:wght@400;600;700&family=Oswald:wght@300;500&family=Arimo:wght@400;700&family=Nothing+You+Could+Do&display=swap">
<style>
:root{
  --blue:#0a6fbf;
  --pink:#e3147a;
  --yellow:#f6c51a;
  --orange:#f5a623;
  --ink:#3a3a3a;
  --btn-green-top:#3bcc16;
  --btn-green-bot:#1d9a00;
  --text:#555;
  --nav:#555;
  --caption-bg:rgba(150,150,150,.78);
  --footer-bg:#f2f2f2;
  --bar-bg:#e9e9e9;
  --muted:#999;
}
*{box-sizing:border-box;margin:0;padding:0}
html,body{width:1093px;height:1200px;overflow:hidden}
body{position:relative;background:#fff;font-family:"Open Sans",sans-serif;color:var(--text)}
.abs{position:absolute}

.site-header{left:0;top:0;width:1093px;height:92px;background:linear-gradient(#fff,#f1f1f1)}
.brand{left:120px;top:28px;display:flex;align-items:center;gap:10px}
.brand-mark{width:12px;height:12px;background:var(--ink)}
.brand-name{font-family:"Open Sans",sans-serif;font-weight:600;font-size:28px;color:var(--ink);line-height:1}
.main-nav{left:653px;top:0;display:flex;height:92px}
.main-nav a{display:flex;align-items:center;justify-content:center;height:92px;font-size:14.5px;font-weight:600;color:var(--nav);text-decoration:none;border-right:1px solid #e2e2e2}
.main-nav a.current{background:#e6e6e6;border-left:1px solid #ddd}
.nav-home{width:100px}.nav-about{width:103px}.nav-contact{width:118px}

.stripe{height:3px}
.hero{left:0;top:95px;width:1093px;height:460px;background:linear-gradient(100deg,#f7f7f7 0%,#f1f1f1 40%,#e8d8c8 62%,#d9c3ab 78%,#c9d2da 100%)}
.caption{background:var(--caption-bg);color:#fff;white-space:nowrap}
.cap-kicker{left:120px;top:184px;width:193px;height:49px;font-family:"Oswald",sans-serif;font-weight:500;font-size:38px;line-height:49px;padding-left:11px}
.cap-title{left:120px;top:238px;width:434px;height:50px;font-family:"Arimo",sans-serif;font-weight:700;font-size:33px;line-height:50px;padding-left:12px}
.cap-sub{left:120px;top:291px;width:451px;height:49px;font-family:"Oswald",sans-serif;font-weight:300;font-size:19px;line-height:49px;padding-left:10px}
.learn-btn{left:120px;top:361px;width:202px;height:44px;border-radius:3px;background:linear-gradient(var(--btn-green-top),var(--btn-green-bot));color:#fff;font-family:"Arimo",sans-serif;font-size:19px;text-align:center;line-height:44px}
.dot{top:426px;width:8px;height:8px;border-radius:50%;background:#ccc;border:1px solid #aaa}
.dot.on{background:var(--pink);border-color:var(--pink)}

.below-hero{left:0;top:555px;width:1093px;height:385px;background:linear-gradient(#e6e6e6,#fafafa 40px,#fff)}
.site-footer{left:0;top:940px;width:1093px;height:223px;background:var(--footer-bg)}
.legal-bar{left:0;top:1163px;width:1093px;height:37px;background:var(--bar-bg);border-top:1px solid #ddd}

.panel{left:120px;top:511px;width:854px;height:446px;background:#fff;box-shadow:0 8px 10px -6px rgba(0,0,0,.35)}
.column{top:0;width:250px}
.column h2{margin-top:21px;font-size:18px;font-weight:700;line-height:20px}
.photo{margin-top:12px;width:244px;height:108px;border:1px solid #ccc}
.column p,.column li{font-size:11.2px;line-height:15.4px;margin-top:16px}
.column ul{list-style:none}
.column li{display:flex;gap:8px;margin-top:15px}
.column li svg{flex:none;margin-top:1px}
.read-more{position:absolute;top:373px;width:108px;height:31px;border:1px solid #ccc;border-radius:3px;background:linear-gradient(#fff,#ececec);font-size:11px;color:var(--blue);text-align:center;line-height:29px}

.connect{left:0;top:985px;width:1093px;text-align:center;font-family:"Nothing You Could Do",cursive;font-size:15px;color:#777}
.social{top:1030px;width:28px;height:28px;border-radius:50%;background:#7a7a7a}
.rule{left:333px;top:1084px;width:427px;height:1px;background:#e2e2e2}
.foot-nav{top:1107px;font-size:11.2px;color:#555}
.copyright{left:120px;top:1175px;font-size:10.5px;color:var(--muted)}
.legal-links{right:119px;top:1175px;font-size:10.5px;color:var(--muted)}
.legal-links span{margin:0 12px}
</style>
</head>
<body>

<header class="site-header abs">
  <div class="brand abs"><span class="brand-mark"></span><span class="brand-name">Alderbrook Advisors</span></div>
  <nav class="main-nav abs">
    <a class="nav-home current" href="#">HOME</a>
    <a class="nav-about" href="#">ABOUT</a>
    <a class="nav-contact" href="#">CONTACT</a>
  </nav>
</header>
<div class="stripe abs" style="left:0;top:92px;width:365px;background:var(--blue)"></div>
<div class="stripe abs" style="left:365px;top:92px;width:364px;background:var(--pink)"></div>
<div class="stripe abs" style="left:729px;top:92px;width:364px;background:var(--yellow)"></div>

<section class="hero abs" role="img" aria-label="Photo of a smiling businesswoman on the phone holding papers in a bright office"></section>
<div class="caption cap-kicker abs">I EXPECT</div>
<div class="caption cap-title abs">Contrary to popular belief</div>
<div class="caption cap-sub abs">Lorem Ipsum is simply dummy text of the printing typesetting</div>
<div class="learn-btn abs">Learn More</div>
<span class="dot abs" style="left:195px"></span>
<span class="dot abs" style="left:215px"></span>
<span class="dot on abs" style="left:235px"></span>

<div class="below-hero abs"></div>
<footer class="site-footer abs"></footer>
<div class="legal-bar abs"></div>

<main class="panel abs">
  <div class="stripe abs" style="left:0;top:0;width:284px;background:var(--blue)"></div>
  <div class="stripe abs" style="left:284px;top:0;width:285px;background:var(--pink)"></div>
  <div class="stripe abs" style="left:569px;top:0;width:285px;background:var(--yellow)"></div>

  <section class="column abs" style="left:21px">
    <h2 style="color:var(--blue)">About Us</h2>
    <div class="photo" role="img" aria-label="City skyline with glass towers under a pale blue sky" style="background:linear-gradient(#bcd3e6,#d6e2ea 55%,#8a9299)"></div>
    <p>You have probably noticed when you receive documents in the mail a majority of senders, in their efforts to decrease expenses, promote paperless solutions.</p>
    <p>Even though paperless technology has been in existence for decades only 17% of document recipients opt in.</p>
    <p>Clearly, people prefer paper.</p>
    <span class="read-more" style="left:1px">+ Read More</span>
  </section>

  <section class="column abs" style="left:305px">
    <h2 style="color:var(--pink)">Features</h2>
    <div class="photo" role="img" aria-label="Business colleagues reviewing documents together at a meeting" style="background:linear-gradient(90deg,#4a4a4a,#cfc9c2 45%,#8c949c)"></div>
    <p>Enough margin to reimburse eated to satisfy the needs of the recipients while also decreasing the senders' costs.</p>
    <ul>
      <li><svg width="13" height="13" viewBox="0 0 13 13"><circle cx="6.5" cy="6.5" r="6" fill="#5cb84a"/><path d="M3.6 6.7l2 2 3.8-4" stroke="#fff" stroke-width="1.5" fill="none"/></svg><span>Delivery anywhere in the world at a fraction of the cost.</span></li>
      <li><svg width="13" height="13" viewBox="0 0 13 13"><circle cx="6.5" cy="6.5" r="6" fill="#5cb84a"/><path d="M3.6 6.7l2 2 3.8-4" stroke="#fff" stroke-width="1.5" fill="none"/></svg><span style="white-space:nowrap">Satisfaction of recipients' paper preferences.</span></li>
      <li><svg width="13" height="13" viewBox="0 0 13 13"><circle cx="6.5" cy="6.5" r="6" fill="#5cb84a"/><path d="M3.6 6.7l2 2 3.8-4" stroke="#fff" stroke-width="1.5" fill="none"/></svg><span>Enough margin to reimburse the recipient for their paper and toner.</span></li>
    </ul>
    <span class="read-more" style="left:1px">+ Read More</span>
  </section>

  <section class="column abs" style="left:588px">
    <h2 style="color:var(--orange)">Our Team</h2>
    <div class="photo" role="img" aria-label="Group of smiling business professionals looking up at the camera" style="background:linear-gradient(#d8dadc,#3a3e46 60%,#c8ccd0)"></div>
    <p>Ut tincidunt mauris nec erat accumsan tempus. Aenean eu odio vitae neque ornare auctor sit amet sed massa.</p>
    <p>Nullam laoreet justo ac fermentum convallis. Mauris elementum nibh sit amet massa lacinia pulvinar.</p>
    <p>Phasellus vel augue sed ipsum aliquam fermentum.</p>
    <span class="read-more" style="left:1px">+ Read More</span>
  </section>
</main>

<div class="connect abs">Get Connected with us !</div>
<span class="social abs" style="left:461px" aria-label="Social profile 1"></span>
<span class="social abs" style="left:509px" aria-label="Social profile 2"></span>
<span class="social abs" style="left:556px" aria-label="Social profile 3"></span>
<span class="social abs" style="left:604px" aria-label="Social profile 4"></span>
<div class="rule abs"></div>
<a class="foot-nav abs" style="left:446px">Home</a>
<a class="foot-nav abs" style="left:526px">About</a>
<a class="foot-nav abs" style="left:606px">Contact</a>

<div class="copyright abs">© 2014 Company Name. All rights reserved.</div>
<div class="legal-links abs">Terms of Service<span>|</span>Privacy Policy</div>

</body>
</html>
```